Business Card For Life Coaching Business For Men

Take my existing logo and apply it to a business card. I would like the logo to be prominent with stylistic text below reading Life Coaching For Men. Contact info should show as:
Gideon Marsh
gideon@bravepathgrowth.com

```html
<!DOCTYPE html>
<html lang="en">
<head>
<meta charset="utf-8">
<title>Bravepath Growth – Business Card</title>
<link href="https://fonts.googleapis.com/css2?family=Open+Sans:wght@400;700;800&family=Pinyon+Script&display=swap" rel="stylesheet">
<style>
  :root {
    --navy: #03008f;
    --teal: #00837f;
    --steel: #7593b6;
    --paper: #ffffff;
    --backdrop: #2b2b2d;
  }
  * { margin: 0; padding: 0; box-sizing: border-box; }
  html, body {
    width: 1200px; height: 875px; overflow: hidden;
    background: var(--backdrop);
    font-family: "Open Sans", sans-serif;
  }
  .canvas {
    position: relative; width: 1200px; height: 875px;
  }
  .card {
    position: absolute;
    width: 560px; height: 320px;
    background: var(--paper);
    border-radius: 18px;
    overflow: hidden;
  }
  .card--front { left: 90px; top: 70px; }
  .card--back { left: 550px; top: 485px; }

  .brand {
    position: absolute;
    display: flex; align-items: center; gap: 16px;
  }
  .brand__dot {
    width: 64px; height: 64px; border-radius: 50%;
    background: var(--steel);
    flex: none;
  }
  .brand__name {
    color: var(--navy);
    font-weight: 800;
    font-size: 40px;
    line-height: 0.98;
    letter-spacing: 0.5px;
    text-transform: uppercase;
  }
  .card--front .brand { left: 110px; top: 82px; }
  .card--back .brand { left: 52px; top: 54px; }

  .tagline {
    position: absolute; left: 0; right: 0; top: 212px;
    text-align: center;
    font-family: "Pinyon Script", cursive;
    font-size: 40px;
    color: var(--steel);
  }

  .waves { position: absolute; inset: 0; width: 100%; height: 100%; }

  .contact {
    position: absolute; right: 32px; bottom: 34px;
    text-align: right; color: var(--paper);
  }
  .contact__name {
    font-weight: 800; font-size: 24px; letter-spacing: 0.5px;
    text-transform: uppercase;
  }
  .contact__email { font-size: 15px; margin-top: 2px; }
</style>
</head>
<body>
<main class="canvas">

  <section class="card card--front" aria-label="Card front">
    <div class="brand">
      <span class="brand__dot"></span>
      <span class="brand__name">Bravepath<br>Growth</span>
    </div>
    <p class="tagline">Life Coaching For Men</p>
  </section>

  <section class="card card--back" aria-label="Card back">
    <svg class="waves" viewBox="0 0 560 320" preserveAspectRatio="none" aria-hidden="true">
      <path d="M0 262 C120 250 250 235 350 160 C420 108 500 72 560 62 L560 320 L0 320 Z" fill="var(--navy)"/>
      <path d="M0 246 C130 238 230 222 330 155 C410 100 490 62 548 48 C495 66 420 106 345 160 C250 228 140 244 0 254 Z" fill="var(--teal)"/>
      <path d="M0 226 C90 224 170 214 240 190 C180 220 90 234 0 240 Z" fill="var(--steel)"/>
    </svg>
    <div class="brand">
      <span class="brand__dot"></span>
      <span class="brand__name">Bravepath<br>Growth</span>
    </div>
    <div class="contact">
      <p class="contact__name">Gideon Marsh</p>
      <p class="contact__email">gideon@bravepathgrowth.com</p>
    </div>
  </section>

</main>
</body>
</html>
```